Coffee Bag Label

I need a coffee bag label designed (front label and back label):
Our company "Tidy-Pod" imports organic coffee beans direct from a farm on Vorsela Mountain on a private reserve (rainforest) from Jinotega, Nicaragua.
Labels should each be 3 inches x 3 inches (with room on edges for bleed). I want the front label to catch the eye and coordinate well with the coffee bag. The bags sizes are below and pictures are attached.
Bag sizes: Lime green 12 oz bag: 3-3/8" x 2-9/16" x 10-1/4"
Black 2 oz sample stand up pouch: 4" x 6-1/2" + 2-3/8", 2oz (60g)
Black 2lb bag: 5" x 3-3/8" x 15", 2lb (1kg)
Please include as much as possible below on the front label without it looking too wordy:
1) Our logo (it's attached). Feel free to do something creative with just the bean and place "Tidy-Pod" or "Tidy-Pod Coffees" somewhere else. They don't have to be together like in the attached file. The bean can be in the background of the label as well or something else cool like in the form of a cloud over the volcano or as the sun in the sky over the volcano.
2) lime green, burnt orange, dark brown & black
3) Front label should say:
"100% Premium Arabica Nicaraguan Coffee"
"Organic, Rain Forest & Mountain Shade Grown"
Bottom of label:
"Medium Roast"
"Full body, bold flavor, nutty, hints of chocolate, with a distinct & flavorful aroma."
I want one front label file for each size bag: "2 oz" "12 oz" & "32 oz"
Back of the label:
I have uploaded a hand drawn pic of what I am thinking but if you have a better idea please submit it.
Please include as much as possible below without it looking wordy:
Directions on the perfect cup:
***2 Tbsp high quality coffee 6 Oz. cup of pure filtered water
(these can be tied into the hand-drawn picture. I will label the section each one corresponds to)
Organically Grown (sustainable)
Rainforest Grown (sustainable)
Mountain Shade Grown (sustainable)
Hand Picked (select)
Spring Water Washed (select)
Sun Dried (select)
Social Responsibility (profits help fund Bright Path Outreach Nicaragua www.brightpathoutreach.example.org)
Single Source Coffee (Single source)
Traceable Source (single source)
Website: www.Tidy-Pod.example.com
Reason: I have been asked to extend deadline by a few designers.
Thanks,
Joanne Pelter
ages 18-54
- Should have a cool border. Maybe fade from one color to another or have something more original than just a 3x3 square border.

```html
<!DOCTYPE html>
<html lang="en">
<head>
<meta charset="utf-8">
<title>Tidy-Pod Coffee Labels</title>
<link rel="stylesheet" href="https://fonts.googleapis.com/css2?family=Arimo:wght@400;700&family=Gochi+Hand&display=swap">
<style>
  :root {
    --lime: #8fd13a;
    --burnt-orange: #b5562a;
    --light-orange: #f7a94a;
    --dark-brown: #3b2a1c;
    --bark: #4a4232;
    --olive-grey: #8c8a74;
    --paper: #e9e8e2;
    --rust: #7a3a22;
    --cream: #f4f1ea;
    --stage: #e4e2dc;
  }
  * { margin: 0; padding: 0; box-sizing: border-box; }
  html, body { width: 1200px; height: 1200px; overflow: hidden; }
  body { background: var(--stage); font-family: "Arimo", Arial, sans-serif; position: relative; }

  .label { position: absolute; overflow: hidden; box-shadow: 0 3px 10px rgba(0,0,0,.25); }
  .abs { position: absolute; }
  .hand { font-family: "Gochi Hand", cursive; }
  .brand { color: var(--dark-brown); font-family: "Arimo", Arial, sans-serif; font-weight: 400; white-space: nowrap; }

  .tribal-band { left: 0; width: 100%;
    background: linear-gradient(180deg, var(--burnt-orange) 0 14%, var(--bark) 14% 86%, var(--lime) 86% 100%); }

  /* Front label */
  .front { left: 20px; top: 30px; width: 580px; height: 580px; background: var(--paper); }
  .front .claim-band { left: 0; top: 0; width: 100%; height: 50px; background: var(--lime);
    display: flex; align-items: center; justify-content: center; font-size: 24px; color: var(--dark-brown); letter-spacing: .5px; white-space: nowrap; }
  .front .tribal-top { top: 50px; height: 125px; }
  .front .tribal-bottom { top: 412px; height: 103px; transform: scaleY(-1); }
  .front .banner-area { left: 62px; top: 112px; width: 456px; height: 86px; background: var(--bark); }
  .front .premium { left: 0; width: 100%; top: 122px; text-align: center; color: var(--cream); font-size: 26px; }
  .front .origin { left: 0; width: 100%; top: 160px; text-align: center; color: var(--cream); font-size: 17px; letter-spacing: 2px; }
  .front .mark-dot { left: 260px; top: 208px; width: 60px; height: 74px; border-radius: 50%; background: var(--rust); }
  .front .brand { left: 0; width: 100%; top: 290px; text-align: center; font-size: 80px; line-height: 1; }
  .front .tagline { left: 0; width: 100%; top: 384px; text-align: center; font-size: 16px; letter-spacing: 3px; color: var(--rust); }
  .front .size { left: 6px; top: 390px; font-size: 16px; color: var(--dark-brown); }
  .front .roast { left: 0; top: 515px; width: 100%; height: 65px; background: var(--light-orange);
    text-align: center; font-size: 21px; line-height: 1.15; color: var(--dark-brown); padding-top: 5px; }
  .front .roast strong { font-weight: 400; font-size: 27px; }

  /* Back label */
  .back { left: 610px; top: 610px; width: 570px; height: 570px; background: var(--olive-grey); }
  .back .directions { left: 20px; top: 28px; color: var(--cream); }
  .back .directions h2 { font-size: 18px; font-weight: 700; }
  .back .directions p { font-size: 16px; line-height: 1.35; }
  .back .mark-dot { left: 444px; top: 22px; width: 42px; height: 52px; border-radius: 50%; background: var(--rust); }
  .back .brand { left: 380px; top: 80px; width: 172px; text-align: center; font-size: 40px; line-height: 1; }
  .back .tagline { left: 380px; top: 124px; width: 172px; text-align: center; font-size: 10px; letter-spacing: 1.5px; color: var(--rust); }
  .back .tribal-mid { top: 200px; height: 215px; }
  .back .base { left: 0; top: 415px; width: 100%; height: 155px; background: var(--bark); }
  .back .mountain-area { left: 0; top: 490px; width: 100%; height: 80px;
    background: linear-gradient(180deg, var(--bark), var(--olive-grey) 60%, var(--light-orange)); }
  .back .frame { left: 120px; top: 186px; width: 330px; height: 316px; background: var(--paper);
    border: 3px solid var(--cream); border-radius: 56px; box-shadow: 0 0 0 6px rgba(244,241,234,.5); }
  .back .features { left: 120px; top: 210px; width: 330px; list-style: none; text-align: center;
    font-size: 19px; line-height: 29px; color: var(--dark-brown); white-space: nowrap; }
</style>
</head>
<body>

<section class="label front" aria-label="Front label">
  <div class="abs claim-band hand">ORGANIC, RAIN FOREST &amp; MOUNTAIN SHADE GROWN</div>
  <div class="abs tribal-band tribal-top" role="img" aria-label="Tribal diamond pattern band in lime, burnt orange and brown"></div>
  <div class="abs tribal-band tribal-bottom" role="img" aria-label="Tribal diamond pattern band in lime, burnt orange and brown"></div>
  <div class="abs banner-area" role="img" aria-label="Distressed brown ribbon banner"></div>
  <div class="abs premium">100% PREMIUM</div>
  <div class="abs origin">ARABICA NICARAGUAN COFFEE</div>
  <div class="abs mark-dot"></div>
  <div class="abs brand">Tidy-Pod</div>
  <div class="abs tagline">ORGANIC COFFEE</div>
  <div class="abs size">12 oz</div>
  <div class="abs roast"><strong>MEDIUM ROAST</strong> full body, bold flavor, nutty,<br>hints of chocolate, with a distinct &amp; flavorful aroma.</div>
</section>

<section class="label back" aria-label="Back label">
  <div class="abs directions">
    <h2>DIRECTIONS ON THE PERFECT CUP</h2>
    <p>2 Tbsp high quality coffee</p>
    <p>6 oz cup of pure filtered water</p>
  </div>
  <div class="abs mark-dot"></div>
  <div class="abs brand">Tidy-Pod</div>
  <div class="abs tagline">ORGANIC COFFEE</div>
  <div class="abs tribal-band tribal-mid" role="img" aria-label="Tribal diamond pattern band in lime, burnt orange and brown"></div>
  <div class="abs base"></div>
  <div class="abs mountain-area" role="img" aria-label="Mountain range illustration in grey and orange"></div>
  <div class="abs frame"></div>
  <ul class="abs features hand">
    <li>ORGANICALLY GROWN</li>
    <li>RAINFOREST GROWN</li>
    <li>MOUNTAIN SHADE GROWN</li>
    <li>HAND PICKED</li>
    <li>SPRING WATER WASHED</li>
    <li>SUN DRIED</li>
    <li>GROWERS WITH SOCIAL RESPONSIBILITY</li>
    <li>SINGLE SOURCE COFFEE</li>
    <li>TRACEABLE SOURCE</li>
  </ul>
</section>

</body>
</html>
```